Make a CV more classy for an orthopaedic hand surgeon

I actually don't want a resume with many pictures etc. I want a CV that is classy, and would be attractive to lawyers. I want you to keep the same content in my current CV just rearrange things if necessary and make it nice, with nice headers and organization. Again, like the sleek, classy, luxury, but professional look. I want lawyers and other recruiters to look at my CV and know I am high class

Target Market(s)

Lawyers, Consulting gigs--they want to see that I am smart and have a lot of accolades

Industry/Entity Type

Medicine

Colors
0054AA
0677BA
7BADD7
CADEEF
E8F1F8

Requirements
Must have
• Classy, luxury, professional
Nice to have
• NA
Should not have
• Additional photos, resume-type look--bubbles everywhere, boxes circled. Should look like the format it is in already, just spiced up and organized better with nice fancy headers and sleek look

```html
<!DOCTYPE html>
<html lang="en">
<head>
<meta charset="utf-8">
<title>Renata Vale, M.D. — Curriculum Vitae</title>
<link href="https://fonts.googleapis.com/css2?family=Montserrat:ital,wght@0,400;0,500;0,600;0,700;1,400&display=swap" rel="stylesheet">
<style>
:root{
  --backdrop:#8b7d75;
  --paper:#ffffff;
  --ink:#1a1a1a;
  --band:#000000;
  --head-bg:#ececec;
}
*{box-sizing:border-box;margin:0;padding:0}
html,body{width:1200px;height:2655px;overflow:hidden}
body{background:var(--backdrop);font-family:'Montserrat',sans-serif;color:var(--ink);position:relative}
.page{position:absolute;width:534px;height:747px;background:var(--paper);box-shadow:0 2px 6px rgba(0,0,0,.18);overflow:hidden}
.page-1{left:48px;top:996px}
.page-2{left:618px;top:996px}
.page-3{left:333px;top:1781px}
.bar-top{position:absolute;left:26px;top:0;width:481px;height:28px;background:var(--band)}
.bar-bottom{position:absolute;left:25px;bottom:0;width:483px;height:26px;background:var(--band)}
.name{position:absolute;left:26px;top:50px;font-size:26px;font-weight:700;letter-spacing:.5px}
.title{position:absolute;left:26px;top:84px;font-size:7.5px;font-weight:700;letter-spacing:.2px}
.contact{position:absolute;left:359px;top:42px;font-size:7px;font-weight:500}
.contact dl{display:grid;grid-template-columns:44px 1fr;row-gap:3px}
.contact dt{font-weight:700}
.contact .gap{height:6px;grid-column:1/3}
.cert-band{position:absolute;left:26px;top:116px;width:481px;height:19px;background:var(--band);color:#fff;font-size:7.5px;font-weight:600;padding:5px 8px}
.col{position:absolute;font-size:6.8px;line-height:1.4}
.col-left{left:26px;top:158px;width:220px}
.col-right{left:283px;top:158px;width:224px}
.sec-head{background:var(--head-bg);font-size:8.4px;font-weight:600;text-transform:uppercase;padding:3px 4px;line-height:1.2;margin-bottom:10px}
.entries{display:grid;grid-template-columns:100px 1fr;row-gap:9px;margin-bottom:14px}
.col-right .entries{grid-template-columns:54px 1fr;row-gap:7px}
.when{font-weight:500;white-space:nowrap}
.what i{font-style:italic}
.lead{position:absolute;left:26px;width:481px;font-size:6.8px;line-height:1.35}
.page-1 .lead{top:602px}
.lead .entries{grid-template-columns:65px 1fr;row-gap:3px}
.page-2 .lead{top:40px}
.page-2 .lead .entries{row-gap:5px}
.sec-head small{font-size:5.5px;font-style:italic;font-weight:700;text-transform:none}
.refs{font-size:6.6px;line-height:1.45}
.refs p{margin-bottom:9px}
.refs b{font-weight:700}
.sec-block{position:absolute;left:26px;width:481px}
.chapters{top:244px}
.articles{top:383px}
.presentations{top:38px}
</style>
</head>
<body>

<section class="page page-1">
  <div class="bar-top"></div>
  <h1 class="name">RENATA VALE, M.D.</h1>
  <p class="title">ORTHOPAEDIC HAND AND UPPER EXTREMITY SURGEON</p>
  <div class="contact">
    <dl>
      <dt>ADDRESS:</dt><dd>4820 Harbor Pointe Dr, Suite 310<br>Linwood, FL 33400</dd>
      <span class="gap"></span>
      <dt>PHONE:</dt><dd>555-010-1221</dd>
      <dt>FAX:</dt><dd>555-010-1231</dd>
      <dt>CELL:</dt><dd>555-010-7527</dd>
    </dl>
  </div>
  <div class="cert-band">BOARD CERTIFIED, HAND SUBSPECIALTY CERTIFIED</div>

  <div class="col col-left">
    <h2 class="sec-head">Education:</h2>
    <div class="entries">
      <span class="when">8/2005 - 5/2009</span><span class="what">BS - Halloway University</span>
      <span class="when">8/2009 - 5/2013</span><span class="what">MD - Brookmere University<br>School of Medicine and Dentistry</span>
    </div>
    <h2 class="sec-head">Post-Graduate Training and<br>Fellowship Appointments:</h2>
    <div class="entries">
      <span class="when">6/2013 - 7/2018</span><span class="what">Resident in Orthopaedic Surgery<br><i>Whitcombe Harbor Hospital,<br>Harborview</i></span>
      <span class="when">8/2018 - 7/2019</span><span class="what">Fellow in Hand Surgery<br><i>Linden University Hospital,<br>Linden City</i></span>
    </div>
    <h2 class="sec-head">Employment History:</h2>
    <div class="entries">
      <span class="when">9/2019 - 9/2021</span><span class="what">Hand &amp; Upper Extremity<br>Orthopaedic Surgeon<br><i>Southeast Meridian<br>Medical Group, Ashford GA</i></span>
      <span class="when">10/2021 - PRESENT</span><span class="what">Hand &amp; Upper Extremity<br>Orthopaedic Surgeon<br>Owner, RV Hand &amp; Upper<br>Extremity Surgery PLLC</span>
    </div>
    <h2 class="sec-head">Board Certification:</h2>
    <div class="entries">
      <span class="when">11/2021 – PRESENT</span><span class="what">National Board of Orthopaedic<br>Surgery (NBOS), Certified in<br>Orthopaedic Surgery</span>
      <span class="when">8/2022</span><span class="what">NBOS, Certified in Surgery of<br>the Hand</span>
    </div>
  </div>

  <div class="col col-right">
    <h2 class="sec-head">Memberships in Professional<br>and Scientific Societies:</h2>
    <div class="entries">
      <span class="when">2019</span><span class="what">NSSH Member</span>
      <span class="when">2016</span><span class="what">NSSH Resident Candidate Member</span>
      <span class="when">2015</span><span class="what">Resident member, OsteoTrauma</span>
      <span class="when">2013</span><span class="what">Resident Member, Whitcombe Harbor Hospital<br>Minority Housestaff Organization</span>
      <span class="when">2013</span><span class="what">Resident Member, Continental Academy of<br>Orthopaedic Surgeons</span>
      <span class="when">2009</span><span class="what">Future Physicians Alliance (FPA)</span>
    </div>
    <h2 class="sec-head">Awards, Honors and Membership in<br>Honorary Societies:</h2>
    <div class="entries">
      <span class="when">2019 - 2021</span><span class="what">6 time "Rock Star Provider of the Month"<br>Award Recipient at Meridian</span>
      <span class="when">2016</span><span class="what">Recipient, Adrian E. Holt National Society<br>of Surgery of the Hand (NSSH) Scholarship</span>
      <span class="when">2016 NEW</span><span class="what">Appointed to Graduate Medical Education<br>Committee (GMEC), Whitcombe Harbor Hospital</span>
      <span class="when">2013</span><span class="what">Whitcombe School of Medicine Excellent Teaching<br>Resident Award</span>
      <span class="when">2009</span><span class="what">Lansing Fellowship Scholarship Recipient,<br>Brookmere University School of Medicine<br>and Dentistry</span>
      <span class="when">2006 - 2009</span><span class="what">Dean's List, Halloway</span>
      <span class="when">2005</span><span class="what">United Racquet Association (URA)<br>Dwight Marlow Scholarship Recipient</span>
      <span class="when">2005</span><span class="what">Key-Note Speaker, Harbor Open Tennis<br>Championship Opening Night Gala</span>
    </div>
  </div>

  <div class="lead">
    <h2 class="sec-head">Leadership, Mentorship, and Work Experience:</h2>
    <div class="entries">
      <span class="when">2022</span><span class="what">Physician Panelist, Planting Roots: Bone and Joint Careers. 2022 FPA Annual Physician Pathways Summit<br>(APPS), Bayside, FL.</span>
      <span class="when">2016-2018</span><span class="what">Resident Representative, Graduate Medical Education Committee (GMEC), Whitcombe Harbor Hospital</span>
      <span class="when">2015-2018</span><span class="what">Instructor, Musculoskeletal Workshops, Whitcombe School of Medicine</span>
      <span class="when">2015</span><span class="what">Assistant-coordinator/Instructor, Physician Assistant Orthopaedic Maneuvers Workshops, Whitcombe School of Medicine</span>
      <span class="when">2015</span><span class="what">Co-coordinator/Presenter, American Medical Alliance (AMA)<br>Middle School Premedical Education Day</span>
    </div>
  </div>
  <div class="bar-bottom"></div>
</section>

<section class="page page-2">
  <div class="lead">
    <h2 class="sec-head">Leadership, Mentorship, and Work Experience <small>(cont...)</small></h2>
    <div class="entries">
      <span class="when">2011-2012</span><span class="what">Coordinator, Future Physicians Alliance Annual Pre-Medical Conference,<br>Brookmere University School of Medicine and Dentistry</span>
      <span class="when">2010</span><span class="what">Coordinator/Master Instructor, Young Scientists Bridge Program,<br>Brookmere University School of Medicine and Dentistry</span>
      <span class="when">2010</span><span class="what">Creator/Organizer, Brookmere University Medical Center Charity Fashion Show,<br>Brookmere University Medical Center</span>
      <span class="when">2009-2011</span><span class="what">Medical Assistant, BU Well St. Brigid's Neighborhood Center,<br>Brookmere University</span>
      <span class="when">2009-2011</span><span class="what">Mentor, Pre-Health Scholars Circle (PHSC),<br>Brookmere University School of Medicine and Dentistry</span>
      <span class="when">2009</span><span class="what">Team Captain, Halloway University Women's Tennis Team</span>
      <span class="when">2008-2009</span><span class="what">Teaching Assistant, Physics 1101/1102 Course, Halloway University</span>
      <span class="when">2008-2009</span><span class="what">Biology Student Advisor, College of Agriculture and Life Sciences at Halloway University</span>
      <span class="when">2004-2005</span><span class="what">Health Talk Show Host, WKRV Radio Station, #1 hip-hop and R&amp;B Radio Station, Brookmere, NY</span>
    </div>
  </div>

  <div class="sec-block chapters refs">
    <h2 class="sec-head">Book Chapters:</h2>
    <p><b>Vale R,</b> Doran SD. Ulnar-Sided Wrist Cartilage Injuries. Chapter 24. In Elmore and Akers, ed. Principles of Wrist Injury Care. Linden City: Harbor Medical Press (in Press 2018).</p>
    <p><b>Vale R,</b> Sharpe MS. Soft Tissue Infections of the Foot. In Acute Care of Infectious Conditions, 2nd Edition. Editor: Rachel Cho, MD. Brookmere Academic Press. In Press 2018.</p>
    <p><b>Vale R.</b> &amp; Carden, C.W. (in press). Clinical Views on Skill Growth in Young Athletes. In J. Barker, S. Colby, J. Shore &amp; N. Watts (Eds.). The Lindell Guide to Athletic Potential and Growth. Eastport: Lindell. In Press 2016.</p>
    <p><b>Vale R,</b> Sharpe MS. Bone Infections. In Acute Care of Infectious Conditions, 2nd Edition.</p>
  </div>

  <div class="sec-block articles refs">
    <h2 class="sec-head">Articles Accepted, Submitted, or in Preparation:</h2>
    <p>Nolan DM, Bowen AL, Alden MK, <b>Vale R,</b> Knox GM, Doran SD. Bridge Plate Fixation for Carpal Dislocation Injuries. J Hand Wrist Res. 2021 May 11;11(1): 16-20. Doi: 10.1000/s-0041-1700000. PMID: 35100000; PMCID: PMC8800000.</p>
    <p>Malik R, <b>Vale R. S.,</b> Mercer M. R., Olsen T. D., Nwosu A. M., Webber M. L., &amp; Graves J. N. (2020). Return Admissions After Operative Wrist Fracture Repair: A Review of 11,124 Cases. Glob Orthop Res Rev, 4(7), e20.</p>
    <p>Azar SC, <b>Vale R,</b> Chawla AN, Baker BJ, Zelinsky IJ, Levine LS (2020). National Society for Surgery of the Hand (NSSH) Leadership Addresses, 1964-2018: Looking Back at Our Roots While Looking Ahead. Hand Surg Open, 2(4):246-249. doi: 10.1000/.-hso.2020.04.006. Epub 2020 Apr 22.</p>
    <p><b>Vale R,</b> Carden C, Sharpe MS, Nwosu N (2019). Clinical Review: Nerve Disorders Around the Shoulder in Youth Sports. Sports Med Rev. 48(2) 131-141.</p>
    <p><b>Vale R,</b> Greer J, Nichols A, Sharpe MS (2018). Growth Modulation for Bowed Legs in a Child with Short Stature Dysplasia: Case Report and Literature Review. Reg Med J. 82(5), 265-268.</p>
    <p>Nielsen S, <b>Vale R,</b> Kegan K. Extra Incisions in Front-Approach Hip Replacement Surgery. Continental Academy of Orthopaedic Surgeons 2017 Orthopaedic Video Theater.</p>
    <p>Kohl R, <b>Vale R,</b> Lawton J, Moore C, &amp; Nicolai G (2014). Scope Skills Teaching Tools in Orthopaedic Residency Programs. Knee Surg Rev, 28(01), 067074. doi:10.1000/s-0034-1300000</p>
    <p><b>Vale R,</b> Tobin S. Minimally invasive kidney removal today: Does surgical robotics add value? February 2012-May 2012. Department of Urology: Brookmere University Medical Center. Advisor: Scott Tobin, MD (Abstract).</p>
  </div>
  <div class="bar-bottom"></div>
</section>

<section class="page page-3">
  <div class="sec-block presentations refs">
    <h2 class="sec-head">Presentations:</h2>
    <p><b>Vale R</b> (2022). Managing Carpal Dislocations with Dorsal Bridge Plate Support. 2022 National Society for Surgery of the Hand Annual Meeting. Eastport, MA.</p>
    <p>Sharpe MS, Fenn RS, Cahall S, <b>Vale R,</b> Nwosu A (2017). Gender Gaps in Research Abstract Submissions Within Pediatric Orthopaedic Surgery: A Review of PSNA Submissions 2012 2015. PSNA Annual Meeting. Valmora, Spain</p>
    <p><b>Vale R</b> (2016). Treating Wrist Fractures: Tailoring Care to the Individual Patient. Department of Orthopaedics and Rehabilitation Grand Rounds, Whitcombe University School of Medicine, Harborview CT.</p>
    <p><b>Vale R</b> (2016). Growth Guidance Techniques for Correcting Limb Alignment Problems in Children. Department of Orthopaedic Surgery, Westbury Hospital.</p>
    <p><b>Vale R</b> (2015). Open Questions in Joint Replacement Practice. Department of Orthopaedic Surgery, Westbury Hospital.</p>
    <p><b>Vale R</b> (2015). Metabolic Bone Remodeling Disorders. Department of Orthopaedic Surgery, Westbury Hospital.</p>
    <p><b>Vale R</b> (2015). Realigning Bowed Legs in Young Children: Lessons From a Single Case of Skeletal Dysplasia. Department of Orthopaedics and Rehabilitation Grand Rounds, Whitcombe University School of Medicine, Harborview CT.</p>
    <p><b>Vale R</b> (2011). Reviewing the Scope Skills Teaching Tools Used Across Orthopaedic Residency Programs. Association of National Medical Colleges Conference: Teaching Innovations in Medicine Forum. Pinecrest, Colorado.</p>
    <p>Tobin S, Trivan D, Scosky E, <b>Vale R,</b> Allen B, Adler R, Rashad H, Josephs J, Wen G (2012). Minimally Invasive Kidney Removal Today: Does Surgical Robotics Add Value? Northern Region Urology Resident Forum. Lakeport, New York</p>
  </div>
  <div class="bar-bottom"></div>
</section>

</body>
</html>
```